Visitenkarten-Design für Hausarztpraxis
Zielgruppe
Hausarztpraxis mit Schwerpunkt Geriatrie
Zielgruppe: Patienten in einem eher ländlichen Stadtgebiet mit hoher Anzahl von Senioren
Aufgabenstellung
Idee: Kombination eines Gutscheines für eine Kaffespezialität auf der Rückseite und einer beschreibbaren Vorderseite als Bestellkärtchen mit Foto von zukünftigen "Praxisgängern" im Querschnitt. D.h. Zu sehen sein sollten 1 lustige Oma , 1 lustiger Opa (z.B. Pfeife rauchend), 1 Jugendlicher und diverse andere Erwachsene verschiedener Berufsgruppen. Beispielhaft siehe unter: Tintenfuchs: Online Terminvereinbarung-Die keine Wünsche offen lässt. Das Bild könnte auch "gezeichnet" sein. Ich würde aber ein treffendes Foto bevorzugen. Design: gut leserliche Schrift, keine verschlungene Schriftarten, wegen Lesbarkeit für Renterklientel.
Info auf der Vorderseite mit Foto: WARTEN? Nicht bei uns - Ihr persönlicher Wunschtermin:
Info auf der Rückseite (Gutschein): Gutschein für eine Kaffeespezialität (Kaffeesymbol)
farblich unterlegt, Farbe egal, passend abgestimmt zur Vorderseite
Zur Erklärung:
Die Form/ Grösse sollte die einer Visitenkarte möglichst nicht überschreiten. Gern auch eine grössere Visitenkartenform 10cm breit und 7,5 cm hoch. Das Format ist unserem Zeitdruck geschuldet. Es muss ein Werbemittel in 14 Tagen zur Praxiseröffnung zur Verfügung stehen, was sich schnell und kostengünstig produzieren und bei Bedarf ohne Probleme nachproduzieren lässt.
Sonderformate haben lange Auftragszeiten bei den auszuführenden Werbedruckfirmen.

```html
<!DOCTYPE html>
<html lang="de">
<head>
<meta charset="utf-8">
<title>Terminkarte und Gutschein</title>
<link rel="stylesheet" href="https://fonts.googleapis.com/css2?family=Questrial&display=swap">
<style>
  :root {
    --teal: #97c3c3;
    --white: #ffffff;
    --label: #555555;
    --page: #ffffff;
    --wood-dark: #5a2c15;
    --wood-mid: #8a4a26;
    --wood-light: #a0592e;
  }
  html, body {
    margin: 0;
    padding: 0;
    width: 849px;
    height: 1200px;
    overflow: hidden;
    background: var(--page);
    font-family: "Questrial", "Century Gothic", sans-serif;
  }
  .canvas { position: relative; width: 849px; height: 1200px; }

  .card {
    position: absolute;
    background: var(--teal);
    color: var(--white);
    box-shadow: 3px 4px 6px rgba(0,0,0,0.25);
  }

  /* Terminkarte */
  .appointment-card { left: 73px; top: 60px; width: 687px; height: 445px; }
  .appointment-card .headline {
    position: absolute; left: 35px; top: 14px; margin: 0;
    white-space: nowrap; font-weight: 400; line-height: 1;
  }
  .headline .shout { font-size: 66px; letter-spacing: 1px; }
  .headline .reply { font-size: 44px; margin-left: 8px; }
  .people-strip { position: absolute; left: 0; top: 103px; width: 687px; height: 193px; display: block; }
  .wish-title {
    position: absolute; left: 33px; top: 318px; margin: 0;
    font-size: 40px; font-weight: 400; line-height: 1; white-space: nowrap;
  }
  .field {
    position: absolute; top: 369px; height: 42px; width: 305px;
    background: var(--white); color: var(--label);
    font-size: 24px; line-height: 42px; padding-left: 11px; box-sizing: border-box;
  }
  .field-date { left: 33px; }
  .field-time { left: 349px; }

  /* Gutschein */
  .voucher-card { left: 72px; top: 644px; width: 687px; height: 443px; }
  .voucher-title {
    position: absolute; left: 0; width: 100%; top: 22px; margin: 0;
    text-align: center; font-size: 86px; font-weight: 400; line-height: 1; letter-spacing: 1px;
  }
  .voucher-sub {
    position: absolute; left: 0; width: 100%; top: 108px; margin: 0;
    text-align: center; font-size: 37px; line-height: 1;
  }
  .coffee-table { position: absolute; left: 0; top: 168px; width: 687px; height: 243px; display: block; }
</style>
</head>
<body>
<div class="canvas">

  <section class="card appointment-card">
    <h1 class="headline"><span class="shout">WARTEN?</span><span class="reply">Nicht bei uns</span></h1>

    <svg class="people-strip" viewBox="0 0 687 193" role="img" aria-label="Fotostreifen mit fünf Praxisgängern: überraschter älterer Herr, lachende junge Frau, ältere Dame mit erhobenem Finger, junger Mann mit Fliege und ein Mops mit Pfeife">
      <defs>
        <linearGradient id="p1" x1="0" y1="0" x2="0" y2="1"><stop offset="0" stop-color="#8e8a80"/><stop offset="1" stop-color="#3c4458"/></linearGradient>
        <linearGradient id="p2" x1="0" y1="0" x2="0" y2="1"><stop offset="0" stop-color="#9ea3aa"/><stop offset="1" stop-color="#d8d2b8"/></linearGradient>
        <linearGradient id="p3" x1="0" y1="0" x2="0" y2="1"><stop offset="0" stop-color="#3f5f5c"/><stop offset="1" stop-color="#a53a32"/></linearGradient>
        <linearGradient id="p4" x1="0" y1="0" x2="0" y2="1"><stop offset="0" stop-color="#d6d6d6"/><stop offset="1" stop-color="#4a6488"/></linearGradient>
        <linearGradient id="p5" x1="0" y1="0" x2="0" y2="1"><stop offset="0" stop-color="#3e4e50"/><stop offset="1" stop-color="#cbb89a"/></linearGradient>
      </defs>
      <polygon points="0,0 173,0 113,193 0,193" fill="url(#p1)"/>
      <polygon points="173,0 314,0 254,193 113,193" fill="url(#p2)"/>
      <polygon points="314,0 450,0 390,193 254,193" fill="url(#p3)"/>
      <polygon points="450,0 588,0 528,193 390,193" fill="url(#p4)"/>
      <polygon points="588,0 687,0 687,193 528,193" fill="url(#p5)"/>
    </svg>

    <h2 class="wish-title">Ihr persönlicher Wunschtermin</h2>
    <div class="field field-date">Datum:</div>
    <div class="field field-time">Uhrzeit:</div>
  </section>

  <section class="card voucher-card">
    <h1 class="voucher-title">GUTSCHEIN</h1>
    <p class="voucher-sub">für eine Kaffeespezialität</p>

    <svg class="coffee-table" viewBox="0 0 687 243" role="img" aria-label="Foto: Holztisch mit verstreuten Kaffeebohnen und einer Tasse Kaffee mit Löffel von oben">
      <defs>
        <linearGradient id="wood" x1="0" y1="0" x2="0" y2="1">
          <stop offset="0" stop-color="#8a4a26"/>
          <stop offset="0.6" stop-color="#a0592e"/>
          <stop offset="1" stop-color="#4e2410"/>
        </linearGradient>
      </defs>
      <rect width="687" height="243" fill="url(#wood)"/>
    </svg>
  </section>

</div>
</body>
</html>
```